New Business and Accounting Software need a Web Site

The website is for a Business and Accounting Software that has 8 products.
Each product has its owns logo and color, when you do the design have in consideration that we are looking the experience that when you change from one product page to another the look and feel adjust to the color and logo of the product.
The product are:
Ventas (Sales)
Compras (Purchases)
Contabilidad (Accounting)
Presupuesto (Budget)
Inventarios (Inventory)
Bancos (Banks)
NĂ³mina RH (Human Resources Payroll)
CRM (Customer Relationship Manager)

You can see how the main logo and variations are used in each page
- https://www.ufta.com/
- https://www.vemi.com/
- https://www.prulvin.com/

Our goal is to be similar to them.

I have created a word document to explain what I want.
You need to design:
1 Home Page
1 Product Landing Page
1 Product Detail Page
1 Price Page

I am attaching:
1. Main Logo
2. 8 Product Logos
3. Website Idea, you can create your own idea.

You are welcome to use other icons for the each product if you want.

Target Market(s)

Independet professionals and Small and Medium Companies

Industry/Entity Type

Business and Accounting Software

Coding

Coded - Design and coding required

Colors
0054AA
0677BA
7BADD7
CADEEF
E8F1F8

Requirements
Must have
• Must show all products in the main page

```html
<!DOCTYPE html>
<html lang="en">
<head>
<meta charset="utf-8">
<title>tallo.cr — Business and Accounting Software</title>
<link href="https://fonts.googleapis.com/css2?family=Poppins:wght@300;400;500;600;700&display=swap" rel="stylesheet">
<style>
:root{
  --blue:#0054AA;
  --blue-mid:#0677BA;
  --blue-soft:#7BADD7;
  --blue-pale:#CADEEF;
  --blue-ice:#E8F1F8;
  --ink:#111827;
  --text:#2b2f38;
  --navy:#0b1220;
  --rose:#d0728a;
  --teal:#23969a;
  --mint:#74bd8e;
  --slate:#6f729a;
  --brick:#a85858;
  --orange:#dc8a57;
  --cta-green:#7bbd93;
  --white:#ffffff;
}
*{box-sizing:border-box;margin:0;padding:0}
html,body{width:1200px;height:2954px;overflow:hidden}
body{position:relative;background:var(--white);font-family:'Poppins',sans-serif;color:var(--text)}
.abs{position:absolute}
a{color:inherit;text-decoration:none}

/* header & hero */
.hero{left:0;top:0;width:1200px;height:470px;overflow:hidden}
.hero-photo{position:absolute;inset:0;background:linear-gradient(100deg,#1c3763 0%,#2d5790 40%,#3f6ea8 70%,#2a4a78 100%)}
.hero-wave{position:absolute;left:0;bottom:0;width:1200px;height:110px}
.brand{display:flex;align-items:center;gap:8px;font-weight:600}
.brand-dot{width:34px;height:34px;border-radius:50%;border:4px solid currentColor}
.nav-brand{left:200px;top:14px;color:var(--white);font-size:26px}
.nav{left:522px;top:22px;display:flex;gap:30px;font-size:12.5px;color:var(--white);align-items:center}
.nav .signin{font-weight:600}
.nav-trial{left:912px;top:16px;width:88px;height:30px;background:var(--blue-soft);color:var(--white);font-size:12px;font-weight:500;display:flex;align-items:center;justify-content:center;border-radius:2px}
.hero-title{left:200px;top:136px;width:400px;color:var(--white);font-size:32px;font-weight:300;line-height:36px}
.hero-title b{font-weight:600}
.hero-btn{left:200px;top:270px;width:88px;height:30px;background:var(--white);color:var(--blue);font-size:12px;font-weight:600;display:flex;align-items:center;justify-content:center;border-radius:2px}

/* products */
.products{left:0;top:440px;width:1200px;height:338px;background:linear-gradient(180deg,var(--blue-ice) 0%,var(--blue-ice) 70%,#bcd4ea 100%);z-index:-1}
.product{width:206px;height:74px;display:flex;flex-direction:column;align-items:center;justify-content:flex-end;gap:8px;font-weight:600;color:var(--blue);font-size:19px;letter-spacing:.5px}
.product .mark{width:34px;height:34px;border-radius:50%}
.vline{width:1px;height:74px;background:#c3cfdb}
.hline{width:74px;height:1px;background:#c3cfdb}

/* profiles */
.section-title{width:1200px;left:0;text-align:center;font-size:30px;font-weight:300;color:var(--ink)}
.section-title b{font-weight:600}
.card-photo{background:linear-gradient(135deg,#9aa8b4,#5d6a78 60%,#3c4652)}
.card-text{padding:16px 19px;color:var(--white)}
.card-text h3{font-size:14px;font-weight:500;margin-bottom:14px}
.card-text p{font-size:9.3px;line-height:15px;font-weight:300}
.card-text .more{display:block;margin-top:13px;font-size:9.5px;font-weight:600}

/* tabs */
.tab{height:51px;display:flex;align-items:center;gap:10px;padding-left:14px;color:var(--white);font-size:13.5px;line-height:15px;border-radius:4px 4px 0 0}
.tab .dot{width:22px;height:22px;border-radius:50%;border:3px solid var(--white);flex:none}
.tab.active{background:var(--white);color:var(--blue-soft);border:1px solid var(--blue-soft);border-bottom:none}
.tab.active .dot{border-color:var(--blue)}
.tab-rule{left:0;top:1559px;width:1200px;height:1px;background:var(--blue-soft)}

/* chart of accounts */
.accounts{left:0;top:1560px;width:1200px;height:406px;background:var(--blue-ice)}
.acc-title{left:200px;top:1644px;font-size:23px;font-weight:300;color:var(--ink)}
.acc-list{left:200px;top:1697px;list-style:none;font-size:10px;color:var(--text)}
.acc-list li{height:26px;display:flex;align-items:center;gap:8px}
.btn{height:30px;display:flex;align-items:center;justify-content:center;font-size:12px;font-weight:500;color:var(--white);border-radius:2px}
.acc-photo{left:612px;top:1622px;width:388px;height:282px;background:linear-gradient(135deg,#c8d3dc,#9fb0bf 45%,#7f93a6)}

/* why choose */
.feature{width:185px}
.feature .icon{width:62px;height:62px;border-radius:50%;background:var(--blue);display:flex;align-items:center;justify-content:center}
.feature h4{margin-top:16px;font-size:13.5px;font-weight:500;color:var(--ink)}
.feature p{margin-top:12px;font-size:9.5px;line-height:15px;color:var(--text)}

/* cta */
.cta{left:0;top:2317px;width:1200px;height:281px;background:var(--cta-green);overflow:hidden}
.cta-photo{position:absolute;right:0;top:0;width:400px;height:281px;background:linear-gradient(90deg,var(--cta-green) 0%,#8f8a78 40%,#6a5646 75%,#4a3a30 100%)}
.cta-brand{left:200px;top:2357px;color:var(--white);font-size:24px}
.cta-title{left:200px;top:2436px;color:var(--white);font-size:30px;font-weight:300;line-height:36px}
.cta-title b{font-weight:600}

/* footer */
.footer{left:0;top:2598px;width:1200px;height:356px;background:var(--navy)}
.foot-brand{left:200px;top:2661px;color:var(--blue);font-size:42px}
.foot-brand .brand-dot{width:56px;height:56px;border-width:6px}
.social{width:30px;height:30px;border-radius:50%;background:var(--blue-soft)}
.social.on{background:var(--blue)}
.foot-head{font-size:14px;font-weight:600;color:var(--white)}
.foot-links{list-style:none;font-size:10.5px;color:var(--white)}
.foot-links li{height:22.5px}
.foot-text{font-size:10px;line-height:17px;color:var(--white)}
.input{left:612px;top:2747px;width:338px;height:30px;background:#2a2f3a;color:#d6dae2;font-size:9.5px;display:flex;align-items:center;padding-left:12px}
.copy{left:200px;top:2882px;font-size:9.5px;color:var(--white)}
.copy span{color:var(--blue)}
</style>
</head>
<body>

<!-- Hero -->
<div class="abs hero">
  <div class="hero-photo" role="img" aria-label="Photo of a man working at a desktop monitor showing accounting software, with a blue overlay"></div>
  <svg class="hero-wave" viewBox="0 0 1200 110" preserveAspectRatio="none">
    <path d="M0,70 C120,40 240,20 380,28 C520,36 620,80 760,96 C900,112 1060,95 1200,62 L1200,110 L0,110 Z" fill="#E8F1F8"/>
  </svg>
</div>
<div class="abs brand nav-brand"><span class="brand-dot"></span>tallo.cr</div>
<nav class="abs nav">
  <a>Home</a><a>Solutions &#8964;</a><a>Prices</a><a>Contact us</a><a class="signin">&#9679; Sign In</a>
</nav>
<a class="abs nav-trial">Free Trial</a>
<h1 class="abs hero-title">Lorem Ipsum is <b>simply dummy text</b> the printing industry.</h1>
<a class="abs hero-btn">Free Trial</a>

<!-- Products -->
<div class="abs products"></div>
<div class="abs product" style="left:188px;top:534px"><span class="mark" style="background:#f39a32"></span>VENTAS</div>
<div class="abs product" style="left:394px;top:534px"><span class="mark" style="background:#5aa9de"></span>COMPRAS</div>
<div class="abs product" style="left:600px;top:534px;font-size:15px"><span class="mark" style="background:#9b6fc9"></span>CONTABILIDAD</div>
<div class="abs product" style="left:807px;top:534px;font-size:13px"><span class="mark" style="background:#d9414b"></span>INVENTARIOS</div>
<div class="abs product" style="left:188px;top:637px;font-size:21px"><span class="mark" style="background:#8a8d92"></span>BANCOS</div>
<div class="abs product" style="left:394px;top:637px;font-size:14px"><span class="mark" style="background:#26a88c"></span>PRESUPUESTO</div>
<div class="abs product" style="left:600px;top:637px;font-size:16px"><span class="mark" style="background:#3fb6a9"></span>NÓMINA RH</div>
<div class="abs product" style="left:807px;top:637px;font-size:28px"><span class="mark" style="background:#2f5fb4"></span>CRM</div>
<div class="abs vline" style="left:394px;top:534px"></div>
<div class="abs vline" style="left:600px;top:534px"></div>
<div class="abs vline" style="left:807px;top:534px"></div>
<div class="abs vline" style="left:394px;top:637px"></div>
<div class="abs vline" style="left:600px;top:637px"></div>
<div class="abs vline" style="left:807px;top:637px"></div>
<div class="abs hline" style="left:357px;top:622px"></div>
<div class="abs hline" style="left:563px;top:622px"></div>
<div class="abs hline" style="left:770px;top:622px"></div>

<!-- Profiles -->
<h2 class="abs section-title" style="top:830px">What is your <b>profile?</b></h2>

<div class="abs card-photo" style="left:200px;top:906px;width:250px;height:187px" role="img" aria-label="Photo of two colleagues working at a laptop"></div>
<div class="abs card-text" style="left:200px;top:1093px;width:250px;height:169px;background:var(--rose)">
  <h3>Profesional</h3>
  <p>There are many variations of passages of Lorem Ipsum available, but the majority have suffered alteration in some form, by injected humour, or randomised words which don't look even slightly believable ...</p>
  <a class="more">Explore More</a>
</div>

<div class="abs card-text" style="left:475px;top:906px;width:250px;height:169px;background:var(--teal)">
  <h3>Accountant</h3>
  <p>There are many variations of passages of Lorem Ipsum available, but the majority have suffered alteration in some form, by injected humour, or randomised words which don't look even slightly believable ...</p>
  <a class="more">Explore More</a>
</div>
<div class="abs card-photo" style="left:475px;top:1075px;width:250px;height:187px;background:linear-gradient(135deg,#e4e6e8,#c3c8cc 50%,#9aa3ab)" role="img" aria-label="Photo of a woman writing at a desk with a laptop"></div>

<div class="abs card-photo" style="left:750px;top:906px;width:250px;height:187px" role="img" aria-label="Photo of two colleagues working at a laptop"></div>
<div class="abs card-text" style="left:750px;top:1093px;width:250px;height:169px;background:var(--mint)">
  <h3>Business</h3>
  <p>There are many variations of passages of Lorem Ipsum available, but the majority have suffered alteration in some form, by injected humour, or randomised words which don't look even slightly believable ...</p>
  <a class="more">Explore More</a>
</div>

<div class="abs card-text" style="left:312px;top:1287px;width:275px;height:170px;background:var(--slate)">
  <h3>Micro</h3>
  <p>There are many variations of passages of Lorem Ipsum available, but the majority have suffered alteration in some form, by injected humour, or randomised words which don't look even slightly believable ...</p>
  <a class="more">Explore More</a>
</div>
<div class="abs card-text" style="left:612px;top:1287px;width:276px;height:170px;background:var(--brick)">
  <h3>SME</h3>
  <p>There are many variations of passages of Lorem Ipsum available, but the majority have suffered alteration in some form, by injected humour, or randomised words which don't look even slightly believable ...</p>
  <a class="more">Explore More</a>
</div>

<!-- Tabs -->
<div class="abs tab" style="left:200px;top:1508px;width:190px;background:var(--orange)"><span class="dot"></span>Get Smart Chart<br>of Accounts</div>
<div class="abs tab active" style="left:404px;top:1508px;width:189px;height:52px"><span class="dot"></span>Get Smart Chart<br>of Accounts</div>
<div class="abs tab" style="left:606px;top:1508px;width:190px;background:var(--rose)"><span class="dot"></span>Get Smart Chart<br>of Accounts</div>
<div class="abs tab" style="left:810px;top:1508px;width:190px;background:var(--brick)"><span class="dot"></span>Get Smart Chart<br>of Accounts</div>
<div class="abs tab-rule"></div>

<!-- Chart of accounts -->
<div class="abs accounts"></div>
<h2 class="abs acc-title">Get smart chart of accounts</h2>
<ul class="abs acc-list">
  <li><svg width="11" height="8" viewBox="0 0 11 8"><path d="M1 4l3 3 6-6" fill="none" stroke="#0054AA" stroke-width="1.5"/></svg>Lorem Ipsum is simply dummy text of the printing and typesetting</li>
  <li><svg width="11" height="8" viewBox="0 0 11 8"><path d="M1 4l3 3 6-6" fill="none" stroke="#0054AA" stroke-width="1.5"/></svg>Lorem Ipsum has been the industry's standard dummy text ever since</li>
  <li><svg width="11" height="8" viewBox="0 0 11 8"><path d="M1 4l3 3 6-6" fill="none" stroke="#0054AA" stroke-width="1.5"/></svg>When an unknown printer took a galley of type scrambled make</li>
  <li><svg width="11" height="8" viewBox="0 0 11 8"><path d="M1 4l3 3 6-6" fill="none" stroke="#0054AA" stroke-width="1.5"/></svg>Lorem Ipsum has been the industry's standard dummy text ever since</li>
  <li><svg width="11" height="8" viewBox="0 0 11 8"><path d="M1 4l3 3 6-6" fill="none" stroke="#0054AA" stroke-width="1.5"/></svg>When an unknown printer took a galley of type scrambled make</li>
</ul>
<a class="abs btn" style="left:200px;top:1844px;width:88px;background:var(--blue)">Free Trial</a>
<a class="abs btn" style="left:294px;top:1844px;width:87px;background:var(--blue-soft)">Learn more</a>
<div class="abs acc-photo" role="img" aria-label="Photo of a woman working with a laptop, calculator and binders"></div>

<!-- Why choose -->
<h2 class="abs section-title" style="top:2018px">Why choose <b>tallo.cr</b></h2>
<div class="abs feature" style="left:200px;top:2090px">
  <div class="icon"><svg width="22" height="26" viewBox="0 0 22 26"><path d="M2 1h12l6 6v18H2z" fill="#fff"/><path d="M6 12h10M6 16h10M6 20h10" stroke="#0054AA" stroke-width="2"/></svg></div>
  <h4>Page by use</h4>
  <p>Lorem Ipsum is simply dummy text of the printing and typesetting Lorem Ipsum has been the industry's standard dummy text .</p>
</div>
<div class="abs feature" style="left:406px;top:2090px">
  <div class="icon"><svg width="22" height="26" viewBox="0 0 22 26"><rect x="1" y="3" width="20" height="22" rx="2" fill="#fff"/><rect x="7" y="0" width="8" height="5" rx="1" fill="#fff" stroke="#0054AA"/><path d="M5 11h12M5 15h12M5 19h12" stroke="#0054AA" stroke-width="2"/></svg></div>
  <h4>Without contract</h4>
  <p>Lorem Ipsum is simply dummy text of the printing and typesetting Lorem Ipsum has been the industry's standard dummy text .</p>
</div>
<div class="abs feature" style="left:612px;top:2090px">
  <div class="icon"><svg width="30" height="20" viewBox="0 0 30 20"><path d="M7 19a6 6 0 0 1 0-12 8 8 0 0 1 15-1 6.5 6.5 0 0 1 1 13z" fill="#fff"/></svg></div>
  <h4>On the cloud</h4>
  <p>Lorem Ipsum is simply dummy text of the printing and typesetting Lorem Ipsum has been the industry's standard dummy text .</p>
</div>
<div class="abs feature" style="left:819px;top:2090px">
  <div class="icon"><svg width="30" height="22" viewBox="0 0 30 22"><rect x="2" y="2" width="20" height="14" fill="none" stroke="#fff" stroke-width="3"/><rect x="0" y="17" width="16" height="3" fill="#fff"/><rect x="19" y="7" width="10" height="14" rx="1" fill="#fff" stroke="#0054AA" stroke-width="1.5"/></svg></div>
  <h4>Multiple devices</h4>
  <p>Lorem Ipsum is simply dummy text of the printing and typesetting Lorem Ipsum has been the industry's standard dummy text .</p>
</div>

<!-- CTA -->
<div class="abs cta">
  <div class="cta-photo" role="img" aria-label="Photo of a woman with glasses working on a laptop in a café"></div>
</div>
<div class="abs brand cta-brand"><span class="brand-dot" style="width:52px;height:52px;border-width:6px"></span>tallo.cr</div>
<h2 class="abs cta-title">What are you waiting for to create a<br><b>free account in Tallo.cr?</b></h2>
<a class="abs btn" style="left:200px;top:2527px;width:175px;height:31px;background:var(--blue)">Create a free account</a>

<!-- Footer -->
<footer class="abs footer"></footer>
<div class="abs brand foot-brand"><span class="brand-dot"></span>tallo.cr</div>
<span class="abs social" style="left:219px;top:2743px"></span>
<span class="abs social on" style="left:257px;top:2743px"></span>
<span class="abs social" style="left:294px;top:2743px"></span>
<span class="abs social" style="left:331px;top:2743px"></span>

<h4 class="abs foot-head" style="left:437px;top:2657px">Quick Links</h4>
<ul class="abs foot-links" style="left:437px;top:2699px">
  <li>Home</li><li>Solutions</li><li>Prices</li><li>Contact us</li><li>Terms &amp; Conditions</li><li>Privacy Policy</li>
</ul>

<h4 class="abs foot-head" style="left:612px;top:2657px">Subscribe Newsletter</h4>
<p class="abs foot-text" style="left:612px;top:2697px;width:350px">Lorem Ipsum is simply dummy text of the printing and typesetting lorem Ipsum has been the industry's standard.</p>
<div class="abs input">Enter your email ...</div>
<a class="abs btn" style="left:612px;top:2785px;width:100px;background:var(--blue)">Submit</a>

<svg class="abs" style="left:1089px;top:2662px" width="20" height="24" viewBox="0 0 20 24"><path d="M10 0L20 24 10 17 0 24z" fill="#0054AA"/></svg>

<p class="abs copy">© 2022 <span>Tallo.cr</span> &nbsp;&nbsp; | &nbsp;&nbsp; All Right Reserved</p>

</body>
</html>
```